Shop Sign Design

I am looking for shop signs/billboards for my boutique (Marula Boutique).The attached file shows what I have been trying to achieve. Those are the colour themes, so please incorporate all 4:-#FFFF00-#D4BB96- #001854-#FFFFFF

Font styles to use
Script

Colors
0255a3
eda3c7
fbed22

```html
<!DOCTYPE html>
<html lang="en">
<head>
<meta charset="utf-8">
<title>Marula Boutique – Shop Sign</title>
<link rel="stylesheet" href="https://fonts.googleapis.com/css2?family=Cormorant+Garamond:wght@500&display=swap">
<style>
  :root {
    --pink: #eda3c7;
    --violet: #7d6fb0;
    --blue: #0f55a3;
    --navy: #1e2552;
    --white: #ffffff;
    --yellow: #f2e31b;
    --sand: #d4bb96;
    --serif: "Cormorant Garamond", "Times New Roman", serif;
  }
  html, body {
    margin: 0;
    padding: 0;
    overflow: hidden;
    background: var(--navy);
  }
  .sign {
    position: relative;
    width: 1200px;
    height: 408px;
    overflow: hidden;
    background: linear-gradient(112deg, var(--pink) 0%, var(--violet) 30%, var(--blue) 58%, var(--navy) 100%);
    font-family: var(--serif);
  }
  .brand-mark {
    position: absolute;
    left: 44px;
    top: 58px;
    width: 520px;
    height: 290px;
    display: flex;
    align-items: center;
    justify-content: center;
    margin: 0;
    color: var(--white);
    font-weight: 500;
    font-size: 340px;
    line-height: 1;
    letter-spacing: -8px;
  }
  .brand-name {
    position: absolute;
    left: 574px;
    top: 50px;
    margin: 0;
    color: var(--white);
    font-weight: 500;
    font-size: 143px;
    line-height: 1;
    letter-spacing: 6px;
    display: flex;
    align-items: baseline;
  }
  .brand-dot {
    display: inline-block;
    width: 14px;
    height: 14px;
    margin-left: 0;
    border-radius: 50%;
    background: var(--yellow);
  }
  .tagline {
    position: absolute;
    left: 577px;
    top: 222px;
    margin: 0;
    color: var(--yellow);
    font-weight: 500;
    font-size: 44px;
    line-height: 1;
    letter-spacing: 1.6px;
    white-space: nowrap;
  }
  .web-address {
    position: absolute;
    left: 620px;
    width: 490px;
    top: 308px;
    margin: 0;
    text-align: center;
    color: var(--sand);
    font-weight: 500;
    font-size: 22px;
    line-height: 1.2;
    letter-spacing: 1.5px;
    white-space: nowrap;
  }
</style>
</head>
<body>
  <main class="sign">
    <p class="brand-mark" aria-hidden="true">MB</p>
    <h1 class="brand-name">Boutique<span class="brand-dot" aria-hidden="true"></span></h1>
    <p class="tagline">FRAGRANCE and FASHION</p>
    <p class="web-address">www.MarulaBoutique.example</p>
  </main>
</body>
</html>
```